Smooth on the Corner needs a new flyer

Smooth on the Corner focuses on waxing and is a male and female wax studio (him & her) with colours light grey red white .or open to unisex colours but obviously need to stick to logo attached.. My theme is fun & funky ,.I am thinking cover page and prices on back.i have images that is going on my new website but not sure if i want to keep it easy to focus on prices?
this will go on front ....
First time guest?
Enjoy a complimentry wax ...
for her- indulge in a brow,underarm or bikini line wax
for him-go smooth with a free ear,nose or brow wax

Target Market(s)

18-35

Industry/Entity Type

Beauty Salon

Font styles to use
Sans Serif

Colors
ec1f27
d5d5d5
ffffff

Requirements
Must have
• light grey red and white , fun, unisex
Nice to have
• wow factor
Should not have
• clinical beauty salon feel/ do not favor my current website, i am having it re-done in a fun way.

```html
<!DOCTYPE html>
<html lang="en">
<head>
<meta charset="utf-8">
<title>Smooth on the Corner – Pricelist</title>
<link rel="stylesheet" href="https://fonts.googleapis.com/css2?family=Arimo:wght@400;700&display=swap">
<style>
:root{
  --red:#ec1f27;
  --grey:#d5d5d5;
  --white:#ffffff;
  --ink:#2b2b2b;
  --symbol:#1d1d1d;
}
*{box-sizing:border-box;margin:0;padding:0}
html,body{width:847px;height:1200px;overflow:hidden}
body{font-family:"Arimo",Arial,sans-serif;color:var(--ink);background:var(--white)}
.flyer{position:relative;width:847px;height:1200px;overflow:hidden;
  background:radial-gradient(ellipse at 30% 20%,#ffffff 0%,#f1f1f1 35%,#dcdcdc 70%,#cfcfcf 100%)}
.smoke{position:absolute;inset:0;
  background:linear-gradient(125deg,rgba(255,255,255,.0) 20%,rgba(255,255,255,.7) 40%,rgba(200,200,200,.3) 60%,rgba(255,255,255,.6) 80%)}
.symbol{position:absolute;top:40px;width:110px;height:135px}
.symbol.female{left:180px}
.symbol.male{left:565px}
.column{position:absolute;top:222px;width:370px}
.column.female{left:58px}
.column.male{left:446px}
.column h2{color:var(--red);font-size:26px;font-weight:700;margin-bottom:6px}
.row{display:flex;font-size:14px;line-height:24px;text-transform:uppercase}
.row .item{flex:1}
.row .price{width:62px;text-align:left}
.row.head{text-transform:none;font-size:14px}
.package{margin-top:18px}
.package h3{font-size:14px;font-weight:700;text-align:center;line-height:22px}
.package .row .item{padding-right:6px}
.package .price.right{text-align:left}
.welcome{position:absolute;top:960px;left:0;width:847px;text-align:center;font-size:17px;line-height:24px}
.welcome h2{color:var(--red);font-size:26px;font-weight:400;margin-bottom:4px}
.address{position:absolute;top:1086px;font-size:14px;line-height:22px}
.address.left{left:60px}
.address.right{left:490px}
.web{position:absolute;top:1140px;left:0;width:847px;text-align:center;color:var(--red);font-weight:700;font-size:16px;letter-spacing:.5px}
</style>
</head>
<body>
<main class="flyer">
  <div class="smoke"></div>

  <svg class="symbol female" viewBox="0 0 110 135" aria-hidden="true">
    <circle cx="55" cy="45" r="34" fill="none" stroke="var(--symbol)" stroke-width="13"/>
    <rect x="48.5" y="78" width="13" height="52" fill="var(--symbol)"/>
    <rect x="30" y="100" width="50" height="12" fill="var(--symbol)"/>
  </svg>
  <svg class="symbol male" viewBox="0 0 110 135" aria-hidden="true">
    <circle cx="45" cy="85" r="34" fill="none" stroke="var(--symbol)" stroke-width="13"/>
    <line x1="68" y1="61" x2="100" y2="27" stroke="var(--symbol)" stroke-width="13"/>
    <polygon points="70,12 106,12 106,48" fill="var(--symbol)"/>
  </svg>

  <section class="column female">
    <h2>Female Pricelist</h2>
    <div class="row head"><span class="item"></span><span class="price">Casual</span><span class="price">Club</span></div>
    <div class="row"><span class="item">Brow Shape</span><span class="price">$25.00</span><span class="price">$18.00</span></div>
    <div class="row"><span class="item">Lip or Chin</span><span class="price">$18.00</span><span class="price">$14.00</span></div>
    <div class="row"><span class="item">Lip &amp; Chin</span><span class="price">$27.00</span><span class="price">$21.00</span></div>
    <div class="row"><span class="item">Brow, Lip, Chin &amp; Sides</span><span class="price">$55.00</span><span class="price">$40.00</span></div>
    <div class="row"><span class="item">Lash Tint</span><span class="price">$20.00</span><span class="price">$15.00</span></div>
    <div class="row"><span class="item">Brow Tint</span><span class="price">$16.00</span><span class="price">$12.00</span></div>
    <div class="row"><span class="item">Brazilian</span><span class="price">$65.00</span><span class="price">$48.00</span></div>
    <div class="row"><span class="item">G-String</span><span class="price">$40.00</span><span class="price">$30.00</span></div>
    <div class="row"><span class="item">Bikini Extended</span><span class="price">$25.00</span><span class="price">$18.00</span></div>
    <div class="row"><span class="item">Bikini Standard</span><span class="price">$30.00</span><span class="price">$22.00</span></div>
    <div class="row"><span class="item">Underarms</span><span class="price">$25.00</span><span class="price">$18.00</span></div>
    <div class="row"><span class="item">Full Arms</span><span class="price">$35.00</span><span class="price">$26.00</span></div>
    <div class="row"><span class="item">Half Leg</span><span class="price">$35.00</span><span class="price">$26.00</span></div>
    <div class="row"><span class="item">Full Leg</span><span class="price">$50.00</span><span class="price">$38.00</span></div>

    <div class="package">
      <h3>PACKAGE - RAISING BROWS</h3>
      <div class="row"><span class="item">Brow Shape &amp; Tint</span><span class="price">$33.00</span><span class="price">$29.00</span></div>
    </div>
    <div class="package">
      <h3>PACKAGE - NEW YORK NEW YORK</h3>
      <div class="row"><span class="item">Brow Shape, Brow Tint &amp; Lash Tint</span></div>
      <div class="row"><span class="item"></span><span class="price">$45.00</span><span class="price">$38.00</span></div>
    </div>
    <div class="package">
      <h3>PACKAGE - I AM A DIVA!</h3>
      <div class="row"><span class="item">Brazilian and Brow</span><span class="price">$68.00</span><span class="price">$59.00</span></div>
    </div>
    <div class="package">
      <h3>PACKAGE - SUNRISE &amp; SUNSET</h3>
      <div class="row"><span class="item">Brazilian, Full Leg Wax, Brow &amp;</span></div>
      <div class="row"><span class="item">Underarm</span><span class="price">$124.00</span><span class="price">$105.00</span></div>
    </div>
  </section>

  <section class="column male">
    <h2>Male Pricelist</h2>
    <div class="row head"><span class="item"></span><span class="price">Casual</span><span class="price">Club</span></div>
    <div class="row"><span class="item">Brow Shape</span><span class="price">$25.00</span><span class="price">$18.00</span></div>
    <div class="row"><span class="item">Brow Centre</span><span class="price">$12.00</span><span class="price">$9.00</span></div>
    <div class="row"><span class="item">Lash Tint</span><span class="price">$20.00</span><span class="price">$15.00</span></div>
    <div class="row"><span class="item">Nose or Ears</span><span class="price">$15.00</span><span class="price">$12.00</span></div>
    <div class="row"><span class="item">Brazilian</span><span class="price">$85.00</span><span class="price">$64.00</span></div>
    <div class="row"><span class="item">Buttocks</span><span class="price">$35.00</span><span class="price">$28.00</span></div>
    <div class="row"><span class="item">Speedo</span><span class="price">$35.00</span><span class="price">$26.00</span></div>
    <div class="row"><span class="item">Full Leg</span><span class="price">$65.00</span><span class="price">$48.00</span></div>
    <div class="row"><span class="item">Back &amp; Shoulders</span><span class="price">$65.00</span><span class="price">$48.00</span></div>
    <div class="row"><span class="item">Chest&nbsp;&nbsp;$50.00</span><span class="price"></span><span class="price">$38.00</span></div>
    <div class="row"><span class="item">Chest &amp; Stomach</span><span class="price">$75.00</span><span class="price">$56.00</span></div>
    <div class="row"><span class="item">Full Arm</span><span class="price">$45.00</span><span class="price">$34.00</span></div>
    <div class="row"><span class="item">Underarm</span><span class="price">$25.00</span><span class="price">$18.00</span></div>

    <div class="package">
      <h3>PACKAGE - MR BIG</h3>
      <div class="row"><span class="item">Full Body Wax (Including Brazilian)</span></div>
      <div class="row"><span class="item"></span><span class="price">$270.00</span><span class="price">$234.00</span></div>
    </div>
    <div class="package">
      <h3>PACKAGE - ABU DHABI</h3>
      <div class="row"><span class="item">Full Body Wax (Excluding Brazilian)</span></div>
      <div class="row"><span class="item"></span><span class="price">$206.00</span><span class="price">$179.00</span></div>
    </div>
    <div class="package">
      <h3>PACKAGE - MR SMOOTH</h3>
      <div class="row"><span class="item">Chest,Stomach,Back &amp; Shoulders</span></div>
      <div class="row"><span class="item"></span><span class="price">$105.00</span><span class="price">$86.00</span></div>
    </div>
  </section>

  <section class="welcome">
    <h2>First time guest?</h2>
    <p>Enjoy a complimentry wax...</p>
    <p><em>for her</em>- indulge in a brow,underarm or bikini line wax</p>
    <p><em>for him</em>-go smooth with a free ear,nose or brow wax</p>
  </section>

  <address class="address left">42 Marlow Street Fernvale NSW 2301<br>P: 02 40001234</address>
  <address class="address right">8 Keel Street, Baywood NSW 2291<br>P: 02 40005678</address>

  <p class="web">WWW.SMOOTHONTHECORNER.COM.AU</p>
</main>
</body>
</html>
```